Service Offering

We need a brochure for our financial advisers, the brochure is specifically for clients of an accounting firm. We provide insurance solutions for the accounting firm, but all they will do to generate new business for us is hand their client the brochure. So we will reply on the brochure to convey our service offering. We are in the process of re-branding and we need something fresh and interesting as we are!! Link to our new demo site below:
http://demo.velmar.co.nz/brisk/

This should allow for an idea of our feel. I'll also attach our logo and a powerpoint that we did for them to gain their trust this captures most of what we are offering their clients, shout if you have any questions, thanks

Industry/Entity Type

Accounting

```html
<!DOCTYPE html>
<html lang="en">
<head>
<meta charset="utf-8">
<title>Brisk – Presentation Folder</title>
<link rel="stylesheet" href="https://fonts.googleapis.com/css2?family=Raleway:wght@300;700&family=Roboto:wght@400;700;900&family=Roboto+Condensed:wght@400;700&display=swap">
<style>
  :root{
    --bg:#4a4a4a;
    --paper:#f7f7f5;
    --paper-grey:#dcdcdc;
    --green:#6cb33f;
    --ink:#2b2b2b;
    --ink-soft:#3a3a3a;
  }
  *{box-sizing:border-box;margin:0;padding:0}
  html,body{width:1200px;height:800px;overflow:hidden}
  body{background:var(--bg);font-family:"Roboto",sans-serif;position:relative}

  .folder{position:absolute;left:160px;top:110px;width:880px;height:580px;display:flex;box-shadow:0 20px 40px rgba(0,0,0,.35)}
  .panel{position:relative;width:440px;height:580px;overflow:hidden}

  /* back cover */
  .back-cover{background:var(--paper)}
  .headline{position:absolute;left:26px;top:44px;font-family:"Raleway",sans-serif;font-weight:300;font-size:27px;line-height:1.35;color:var(--ink)}
  .headline strong{color:var(--green);font-weight:700}
  .questions-photo{position:absolute;left:150px;top:190px;width:290px;height:300px;
    background:linear-gradient(180deg,#2f3033 0%,#3c3d3e 45%,#4b4536 70%,#5e4c2c 100%)}
  .contact{position:absolute;right:315px;top:372px;width:130px;text-align:right}
  .contact-title{font-family:"Roboto Condensed",sans-serif;font-weight:700;font-size:17px;letter-spacing:1px;color:var(--green);padding-bottom:4px;border-bottom:2px solid var(--ink)}
  .contact-list{list-style:none;margin-top:12px}
  .contact-item{display:flex;justify-content:flex-end;align-items:flex-start;gap:6px;font-family:"Roboto Condensed",sans-serif;font-size:8.5px;line-height:1.3;color:var(--ink);margin-bottom:12px}
  .contact-item svg{flex:none;width:10px;height:10px;margin-top:1px}
  .social-row{position:absolute;left:14px;right:26px;top:530px;display:flex;align-items:center;gap:12px}
  .social-row .rule{flex:1;border-top:2px dotted var(--green)}
  .social-dot{width:22px;height:22px;border-radius:50%;background:var(--green)}

  /* front cover */
  .front-cover{background:var(--paper-grey)}
  .brand{position:absolute;left:50px;top:24px;display:flex;align-items:center;gap:10px}
  .brand-dot{width:66px;height:66px;border-radius:50%;background:var(--green)}
  .brand-name{font-family:"Roboto",sans-serif;font-weight:400;font-size:50px;line-height:1;color:var(--green)}
  .brand-tagline{position:absolute;left:152px;top:96px;font-size:8.5px;font-weight:700;color:var(--ink-soft)}
  .sunset-photo{position:absolute;left:0;top:150px;width:424px;height:345px;
    background:linear-gradient(180deg,#5e5570 0%,#8a6f78 30%,#f0b060 52%,#c08a3c 68%,#7a5526 100%)}
  .client-name{position:absolute;left:52px;top:510px;font-weight:900;font-size:24px;color:var(--ink)}
  .client-sub{position:absolute;left:52px;top:540px;font-weight:700;font-size:9px;color:var(--green);letter-spacing:.3px}
  .site-url{position:absolute;left:52px;top:560px;font-weight:700;font-size:11px;letter-spacing:3px;color:var(--ink)}
</style>
</head>
<body>
  <div class="folder">
    <section class="panel back-cover">
      <h2 class="headline"><strong>WE</strong> would like to be<br>in your <strong>CORNER...</strong></h2>

      <div class="questions-photo" role="img" aria-label="Dark stormy field photograph with chalk-style 'Any questions?' lettering"></div>

      <div class="contact">
        <h3 class="contact-title">CONTACT US</h3>
        <ul class="contact-list">
          <li class="contact-item"><span>06 555 0142, 021 555 0187</span>
            <svg viewBox="0 0 10 10"><path fill="#6cb33f" d="M1 3c0-1 1-2 4-2s4 1 4 2v1H7V3H3v1H1zM2 5h6l1 4H1z"/></svg></li>
          <li class="contact-item"><span>demo.velmar.co.nz/brisk</span>
            <svg viewBox="0 0 10 10"><g fill="none" stroke="#6cb33f" stroke-width="1"><circle cx="5" cy="5" r="4"/><ellipse cx="5" cy="5" rx="1.8" ry="4"/><path d="M1 5h8"/></g></svg></li>
          <li class="contact-item"><span>14 Harbour Lane<br>Ashford</span>
            <svg viewBox="0 0 10 10"><path fill="#6cb33f" d="M5 1l4 4H8v4H6V6H4v3H2V5H1z"/></svg></li>
        </ul>
      </div>

      <div class="social-row">
        <span class="rule"></span>
        <span class="social-dot"></span>
        <span class="social-dot"></span>
        <span class="social-dot"></span>
        <span class="social-dot"></span>
        <span class="rule"></span>
      </div>
    </section>

    <section class="panel front-cover">
      <div class="brand">
        <span class="brand-dot"></span>
        <span class="brand-name">brisk</span>
      </div>
      <p class="brand-tagline">in sickness and in health</p>

      <div class="sunset-photo" role="img" aria-label="Golden sunset over a grass field with two people standing under a cloudy sky"></div>

      <h1 class="client-name">NORVALE &amp; ASSOCIATES</h1>
      <p class="client-sub">PRESENTATION</p>
      <p class="site-url">www.brisk.kiwi</p>
    </section>
  </div>
</body>
</html>
```